Lorvant Stationary and Branding Documents

Corporate Identity Branding stationary needed for IT Recruiting Firm.

I already have a Logo, business cards and website. I need to get designs completed for the remaining corporate identity documents.

The documentation should use similar colors as my website and business card. The designs should modern and clean.

http://lorvantsystems.example/

Target Market(s)

Information Technology Industry

Industry/Entity Type

Information Technology

Colors
3377b5
0255a3
fbee3e
f78f20
f37122
33a6d7
000000
0592cd

Requirements
Must have
• Letter Head
• Folder Design
• PowerPoint Design
• Invoice
• Envelope
Nice to have
• Proposal
• Flyer
• Brochure
Should not have
• Logo
• Business Cards
• Website

```html
<!DOCTYPE html>
<html lang="en">
<head>
<meta charset="utf-8">
<title>Lorvant Invoice</title>
<link href="https://fonts.googleapis.com/css2?family=Roboto:wght@500;700&family=Source+Code+Pro:wght@400;500&display=swap" rel="stylesheet">
<style>
:root{
  --bg:#cdced0;
  --paper:#ffffff;
  --brand-blue:#0b58a0;
  --accent-orange:#f7a84a;
  --logo-orange:#f37122;
  --dark:#333333;
  --ink:#111111;
  --rule:#222222;
}
*{margin:0;padding:0;box-sizing:border-box}
html,body{width:1200px;height:1200px;overflow:hidden;background:var(--bg)}
body{position:relative;font-family:"Source Code Pro",monospace;color:var(--ink)}
.invoice-page{position:absolute;left:200px;top:34px;width:801px;height:1133px;background:var(--paper);overflow:hidden}
.brand{position:absolute;top:66px;left:0;width:100%;display:flex;justify-content:center;align-items:center;gap:12px}
.brand-mark{width:14px;height:14px;background:var(--logo-orange)}
.brand-name{font-family:"Roboto",sans-serif;font-weight:500;font-size:56px;color:var(--brand-blue);letter-spacing:1px}
.doc-title{position:absolute;top:186px;width:100%;text-align:center;font-family:"Roboto",sans-serif;font-weight:700;font-size:50px;color:var(--brand-blue)}
.sender{position:absolute;left:95px;top:287px;font-size:15px;line-height:20px;font-style:normal}
.contact-list{list-style:none;margin-top:8px;font-size:10.5px;line-height:14px}
.contact-list li{display:flex;align-items:center;gap:6px}
.contact-list svg{width:9px;height:9px;fill:var(--brand-blue)}
.invoice-meta{position:absolute;left:541px;top:291px;width:170px;font-size:14px;line-height:19px;display:grid;grid-template-columns:1fr auto}
.invoice-meta dd{text-align:right}
.line-items{position:absolute;left:109px;top:420px;width:602px;border-collapse:collapse;font-size:15px}
.line-items thead th{background:var(--accent-orange);font-weight:400;height:26px;text-align:left;padding:0 6px}
.line-items tbody tr{height:38.5px;border:1.5px solid var(--rule)}
.line-items td{padding:0 10px}
.line-items .qty{width:86px}
.line-items .price{width:91px}
.line-items .total{width:116px;text-align:right}
.line-items th.price{text-align:center}
.line-items th.total{text-align:right;padding-right:12px}
.payment-info{position:absolute;left:111px;top:677px;font-size:12.5px;line-height:15.5px}
.payment-info .label-email{margin-bottom:4px}
.totals{position:absolute;left:548px;top:677px;width:162px;font-size:12.5px;line-height:21px}
.totals .row{display:flex;justify-content:space-between}
.totals .grand{margin-top:25px;font-size:18px;margin-left:-2px;width:167px}
.closing{position:absolute;left:106px;top:838px}
.closing .thanks{font-size:12.5px}
.closing .terms{font-size:8.5px;margin-top:2px}
.signature{position:absolute;left:543px;top:815px;width:167px;height:48px;border-bottom:1.5px solid var(--dark)}
.signature-area{width:130px;height:30px;margin:6px 0 0 18px;background:linear-gradient(90deg,#e9e9e9,#f4f4f4)}
.footer-band{position:absolute;left:0;top:922px;width:801px;height:211px;background:linear-gradient(180deg,var(--dark) 0%,var(--brand-blue) 45%,var(--brand-blue) 100%)}
</style>
</head>
<body>
<main class="invoice-page">
  <header class="brand">
    <span class="brand-mark"></span>
    <span class="brand-name">Lorvant</span>
  </header>
  <h1 class="doc-title">INVOICE</h1>

  <address class="sender">
    <div>Two Harbor Plaza 410</div>
    <div>9th Avenue SE</div>
    <ul class="contact-list">
      <li><svg viewBox="0 0 10 10"><rect x="0" y="2" width="10" height="6"/></svg>info@lorvantsystems.example</li>
      <li><svg viewBox="0 0 10 10"><path d="M2 0h2l1 3-1.5 1a6 6 0 0 0 2.5 2.5L7 5l3 1v2a2 2 0 0 1-2 2A8 8 0 0 1 0 2a2 2 0 0 1 2-2z"/></svg>5550142876</li>
      <li><svg viewBox="0 0 10 10"><circle cx="5" cy="5" r="5"/></svg>www.lorvantsystems.example</li>
    </ul>
  </address>

  <dl class="invoice-meta">
    <dt>INVOICE #</dt><dd>12121</dd>
    <dt>DATE</dt><dd>10/01/2018</dd>
  </dl>

  <table class="line-items">
    <thead>
      <tr><th class="qty">QTY</th><th>PRODUCT DESCRIPTION</th><th class="price">PRICE</th><th class="total">TOATL</th></tr>
    </thead>
    <tbody>
      <tr><td class="qty">1</td><td>PROJECT Title 1</td><td class="price">$ 50.00</td><td class="total">$250.00</td></tr>
      <tr><td class="qty">2</td><td>PROJECT Title 2</td><td class="price">$ 50.00</td><td class="total">$250.00</td></tr>
      <tr><td class="qty">3</td><td>PROJECT Title 3</td><td class="price">$ 50.00</td><td class="total">$250.00</td></tr>
      <tr><td class="qty">4</td><td>PROJECT Title 4</td><td class="price">$ 50.00</td><td class="total">$250.00</td></tr>
      <tr><td class="qty">5</td><td>PROJECT Title 5</td><td class="price">$ 50.00</td><td class="total">$250.00</td></tr>
    </tbody>
  </table>

  <section class="payment-info">
    <div class="label-email">EMAIL:</div>
    <div>Bank:</div>
    <div>Bank Sort Code:</div>
    <div>Acount Number:</div>
    <div>Payment Reterive:</div>
  </section>

  <section class="totals">
    <div class="row"><span>Subtotal</span><span>$4.250.00</span></div>
    <div class="row"><span>Tax Rate</span><span>0.00%</span></div>
    <div class="row grand"><span>TOTAL</span><span>$415.00</span></div>
  </section>

  <footer class="closing">
    <div class="thanks">THANK YOPU FOR YOUR BUSINESS</div>
    <div class="terms">Payment is due max 7 days after invoice without deduction.</div>
  </footer>

  <div class="signature">
    <div class="signature-area" role="img" aria-label="Handwritten signature"></div>
  </div>

  <div class="footer-band" role="img" aria-label="Decorative footer graphic in dark grey and brand blue"></div>
</main>
</body>
</html>
```